Pelwick Orchards Business Cards

design business cards for our new business should match my Corvane Appraisals business cards

Contact Information for Business Card

2817 N 61st W Pl
Marlow Bend, NV 74389

Requirements
Must have
• should match logo colors

```html
<!DOCTYPE html>
<html lang="en">
<head>
<meta charset="utf-8">
<title>Pelwick Orchards Business Cards</title>
<link rel="stylesheet" href="https://fonts.googleapis.com/css2?family=Orbitron:wght@700&family=Montserrat:wght@400;500;600;700&display=swap">
<style>
  :root {
    --page-bg: #f4f4f4;
    --card-dark: #03504f;
    --card-light: #ffffff;
    --leaf-green: #76c043;
    --sea-teal: #1ba9b0;
    --ink: #1d1d1d;
    --ink-soft: #333333;
    --card-shadow: 0 6px 22px rgba(0, 0, 0, 0.14);
  }
  * { box-sizing: border-box; margin: 0; padding: 0; }
  html, body {
    width: 800px; height: 1200px; overflow: hidden;
    background: var(--page-bg);
    font-family: "Montserrat", sans-serif;
  }
  .canvas { position: relative; width: 800px; height: 1200px; }
  .card {
    position: absolute; left: 80px; width: 640px; height: 365px;
    box-shadow: var(--card-shadow); overflow: hidden;
  }
  .card--front { top: 217px; background: var(--card-dark); }
  .card--back { top: 618px; background: var(--card-light); }

  .front-band {
    position: absolute; left: 0; bottom: 0; width: 100%; height: 7px;
    background: var(--leaf-green);
  }
  .brand-name {
    font-family: "Montserrat", sans-serif; font-weight: 700;
    color: var(--leaf-green); text-transform: uppercase; line-height: 1.05;
  }
  .card--front .brand-name {
    position: absolute; left: 0; right: 0; top: 118px;
    text-align: center; font-size: 50px; letter-spacing: 6px;
  }
  .card--back .brand-name {
    position: absolute; left: 44px; top: 150px;
    font-size: 27px; letter-spacing: 3px;
  }

  .person { position: absolute; left: 324px; top: 76px; }
  .person-name {
    font-family: "Orbitron", sans-serif; font-weight: 700;
    font-size: 22px; letter-spacing: 1px; line-height: 1;
  }
  .person-name .first { color: var(--leaf-green); }
  .person-name .last { color: var(--sea-teal); }
  .person-role {
    margin-top: 10px; font-size: 15px; letter-spacing: 1px;
    color: var(--ink-soft); font-weight: 400;
  }

  .contact-list { position: absolute; left: 324px; top: 152px; list-style: none; }
  .contact-item {
    display: flex; align-items: center; gap: 12px;
    height: 29px; margin-bottom: 3px;
    font-size: 14px; color: var(--ink); letter-spacing: 0.4px;
  }
  .contact-item--address { height: 40px; margin-top: 6px; line-height: 1.3; }
  .contact-item--phone { font-weight: 700; }
  .contact-icon { width: 29px; height: 29px; flex: none; }

  .back-bands { position: absolute; left: 0; bottom: 0; width: 640px; height: 20px; }
</style>
</head>
<body>
<main class="canvas">

  <section class="card card--front" aria-label="Card front">
    <p class="brand-name">Pelwick<br>Orchards</p>
    <div class="front-band"></div>
  </section>

  <section class="card card--back" aria-label="Card back">
    <p class="brand-name">Pelwick<br>Orchards</p>

    <div class="person">
      <h1 class="person-name"><span class="first">DALE</span> <span class="last">MARROW</span></h1>
      <p class="person-role">PRESIDENT</p>
    </div>

    <ul class="contact-list">
      <li class="contact-item contact-item--phone">
        <svg class="contact-icon" viewBox="0 0 30 30" aria-hidden="true">
          <circle cx="15" cy="15" r="13.5" fill="none" stroke="var(--leaf-green)" stroke-width="1.5"/>
          <path d="M10.5 9.5c.8-.8 1.6-.6 2 .1l1 1.8c.3.6.2 1.1-.3 1.5l-.7.6c.6 1.4 1.6 2.5 3 3.1l.6-.7c.4-.5 1-.6 1.5-.3l1.8 1c.7.4.9 1.2.1 2-1.5 1.5-3.6 1-6-1.3-2.4-2.4-3.7-5-2.9-6.4z" fill="var(--sea-teal)"/>
        </svg>
        <span>640-555-0142</span>
      </li>
      <li class="contact-item">
        <svg class="contact-icon" viewBox="0 0 30 30" aria-hidden="true">
          <circle cx="15" cy="15" r="13.5" fill="none" stroke="var(--leaf-green)" stroke-width="1.5"/>
          <rect x="9" y="11" width="12" height="8.5" rx="1" fill="var(--sea-teal)"/>
          <path d="M9.5 11.5 15 16l5.5-4.5" fill="none" stroke="#fff" stroke-width="1.2"/>
        </svg>
        <span>hello@pelwickorchards.com</span>
      </li>
      <li class="contact-item">
        <svg class="contact-icon" viewBox="0 0 30 30" aria-hidden="true">
          <circle cx="15" cy="15" r="13.5" fill="none" stroke="var(--leaf-green)" stroke-width="1.5"/>
          <circle cx="15" cy="15" r="6.5" fill="var(--sea-teal)"/>
          <path d="M8.5 15h13M15 8.5v13M15 8.5c-3 3.5-3 9.5 0 13M15 8.5c3 3.5 3 9.5 0 13" fill="none" stroke="#fff" stroke-width="0.9"/>
        </svg>
        <span>www.pelwickorchards.com</span>
      </li>
      <li class="contact-item contact-item--address">
        <svg class="contact-icon" viewBox="0 0 30 30" aria-hidden="true">
          <circle cx="15" cy="15" r="13.5" fill="none" stroke="var(--leaf-green)" stroke-width="1.5"/>
          <path d="M15 22s-5-5.2-5-8.6a5 5 0 0 1 10 0C20 16.8 15 22 15 22z" fill="var(--sea-teal)"/>
          <circle cx="15" cy="13.4" r="1.8" fill="#fff"/>
        </svg>
        <span>2817 N 61st W Pl<br>Marlow Bend, NV 74389</span>
      </li>
    </ul>

    <svg class="back-bands" viewBox="0 0 640 20" preserveAspectRatio="none" aria-hidden="true">
      <polygon points="0,12 236,12 229,20 0,20" fill="var(--sea-teal)"/>
      <polygon points="258,0 640,0 640,20 236,20" fill="var(--leaf-green)"/>
    </svg>
  </section>

</main>
</body>
</html>
```